Hdmi 4K solution Hidden cable solution for wall hung TV, Flyer

VALPEX is an audio visual company that install cabling into new construction of homes.

Design Objective:
Design a 1-Page flyer on a dark background that needs to represent today's latest picture quality and sound solution. This flyer will be in a take home pack with all other components of a new home build (like, bathrooms, paint colour, carpets, flooring, window furnishing ETC) for clients to choose in the design process of building a new home

- I would like this to look as professional as possible and to stand out once clients Turn to our HDMI flyer.

Would like to see the following CONTENTS on the flyer:
- 4k symbol plus VALPEX logo
- "Brimz" brand Logo voted best quality by intergation experts 2015-16-17-18
- image of a TV mounted on a wall representing a wall hung TV with a line diagram behind it (like seeing through the wall) indicating the cable behind the wall (Tesbrin,dry wall )
- photo attached of a sample input

- Automated, Easy
- No clutter or dangling cables on the wall
- 4k guarantee

- Clean, hidden cables. Easy,
- Fully Tested and ready to go
- Just Plug in and way go DIY When you move in to your home
-Product is used in the following rooms:
* Home theatre
* Dining / living room
* Fire place
* Alfresco cabana
* Pool house
* Office

"Choosing the right HDMI Cable to prewire hasn't been easier"

Aesthetics or Preferred Style:
Looking for life style Sound lounge feel in the flyer (please check attached sample brochure and flyer)

Logo is supplied and would like to keep it somewhere in the flyer please. It has sentimental significance.

Actual photo attached of the product ( HDMI) Input and output)

Target Market(s)

New home buyers upgrading accessories in design studios. This product need to be easily identified as inexperienced sales people are usually selling these in display studios. Represent today's latest version of HDMI and fun clear defining tones/colors and picture. Looking for elegant and professional colours /aesthetics

Other font styles liked:
• see attachments

Requirements
Must have
• This flyer will be in a take home pack with all other components of a new home build ex. bathrooms, paint colour, carpets, flooring, window furnishing ETC for clients to choose in the design process of building a new home.
• I would like this to look as professional as possible and to stand out once clients Turn to our HDMI flyer.
Nice to have
• Elegant feel with dark tones to help bridge the professional finish we do from day to day on site on new homes.
• Easy to read ond captivating to choose the HDMI solution to be installed into the new home
Should not have
• I am happy to try something new and not pedestrian or similar to other people as we have pioneered this type of installation package.

```html
<!DOCTYPE html>
<html lang="en">
<head>
<meta charset="utf-8">
<title>VALPEX HDMI Flyer</title>
<link rel="stylesheet" href="https://fonts.googleapis.com/css2?family=Montserrat:wght@400;500;600;700&display=swap">
<style>
  :root {
    --page-bg: #d4d4d6;
    --flyer-dark: #2a2a2b;
    --flyer-dark-edge: #1e1e1f;
    --accent: #1ea0e0;
    --accent-deep: #0f7fc0;
    --white: #ffffff;
    --ink: #3b3b3d;
    --text-light: #e9e9e9;
  }
  * { box-sizing: border-box; margin: 0; padding: 0; }
  html, body { width: 1200px; height: 1200px; overflow: hidden; }
  body {
    background: var(--page-bg);
    font-family: "Montserrat", Arial, sans-serif;
    position: relative;
  }
  .flyer {
    position: absolute; left: 204px; top: 40px;
    width: 792px; height: 1120px;
    background: radial-gradient(ellipse at 50% 60%, var(--flyer-dark) 0%, var(--flyer-dark-edge) 100%);
    overflow: hidden;
  }
  .tile { position: absolute; border: 3px solid var(--accent); }
  .logo-tile {
    left: 22px; top: 22px; width: 328px; height: 230px;
    background: var(--white); border: none;
    display: flex; align-items: center; justify-content: center; gap: 12px;
  }
  .logo-dot { width: 22px; height: 22px; border-radius: 50%; background: var(--accent); }
  .logo-name { font-size: 44px; font-weight: 600; color: var(--ink); letter-spacing: 1px; }
  .photo { background: linear-gradient(160deg, #f2f2f2 0%, #c9c9c9 55%, #6b4a36 100%); }
  .photo.warm { background: linear-gradient(160deg, #c79a6a 0%, #3a3a3a 45%, #f0f0f0 100%); }
  .photo.green { background: linear-gradient(160deg, #e6e6e6 0%, #6f8f5a 45%, #3a2c22 100%); }
  .icon-badge {
    position: absolute; width: 64px; height: 64px; border-radius: 50%;
    background: var(--accent); display: flex; align-items: center; justify-content: center;
  }
  .banner { position: absolute; left: 190px; top: 530px; width: 410px; height: 68px; }
  .banner-title {
    position: absolute; inset: 0; display: flex; align-items: center; justify-content: center;
    font-size: 44px; font-weight: 700; color: var(--white);
  }
  .features { position: absolute; top: 624px; font-size: 19px; line-height: 25px; color: var(--text-light); list-style: none; }
  .features.left { left: 36px; width: 340px; }
  .features.right { left: 410px; width: 360px; }
  .features li { position: relative; padding-left: 22px; }
  .features li::before, .rooms .tick::before {
    content: ""; position: absolute; left: 0; top: 7px; width: 11px; height: 11px;
    border-radius: 50%; background: var(--accent);
  }
  .divider { position: absolute; left: 392px; top: 620px; width: 2px; height: 112px; background: var(--accent); }
  .product-box {
    position: absolute; left: 22px; top: 822px; width: 748px; height: 180px;
    background: var(--white); border: 3px solid var(--accent);
  }
  .product-strip { position: absolute; left: 0; top: 760px; width: 792px; height: 128px; }
  .rooms-title {
    position: absolute; left: 0; right: 0; top: 897px; text-align: center;
    font-size: 20px; font-weight: 600; color: var(--accent);
  }
  .rooms {
    position: absolute; left: 40px; right: 40px; top: 935px; text-align: center;
    font-size: 19px; line-height: 25px; color: var(--ink);
  }
  .rooms .tick { position: relative; padding-left: 18px; margin: 0 6px; white-space: nowrap; }
  .rooms .tick::before { top: 6px; width: 10px; height: 10px; }
  .tagline {
    position: absolute; left: 0; right: 0; top: 1024px; text-align: center;
    font-size: 28px; font-weight: 700; line-height: 37px; color: var(--white);
  }
  .quote-mark { font-size: 44px; font-family: Georgia, serif; vertical-align: -10px; line-height: 0; }
</style>
</head>
<body>
<main class="flyer">
  <div class="tile logo-tile"><span class="logo-dot"></span><span class="logo-name">VALPEX</span></div>
  <div class="tile photo" style="left:360px;top:22px;width:202px;height:230px" role="img" aria-label="Wall hung TV above a white low cabinet"></div>
  <div class="tile photo warm" style="left:569px;top:22px;width:201px;height:230px" role="img" aria-label="TV mounted on a timber feature wall in a lounge"></div>
  <div class="tile photo" style="left:22px;top:264px;width:242px;height:234px" role="img" aria-label="Wall mounted TV over a white media unit"></div>
  <div class="tile photo warm" style="left:276px;top:264px;width:242px;height:234px" role="img" aria-label="TV on a white brick wall with a media console"></div>
  <div class="tile photo green" style="left:526px;top:264px;width:244px;height:234px" role="img" aria-label="TV showing a landscape above a shelving unit"></div>

  <div class="icon-badge" style="left:534px;top:106px">
    <svg width="34" height="30" viewBox="0 0 34 30" fill="none" stroke="#fff" stroke-width="2.5">
      <path d="M3 10h6l8-7v24l-8-7H3z" fill="#fff"/><path d="M22 9a8 8 0 0 1 0 12M26 5a13 13 0 0 1 0 20"/>
    </svg>
  </div>
  <div class="icon-badge" style="left:234px;top:351px">
    <svg width="32" height="30" viewBox="0 0 32 30" fill="none" stroke="#fff" stroke-width="3">
      <rect x="2" y="2" width="28" height="19" rx="2"/><path d="M16 21v6M10 27h12"/>
    </svg>
  </div>
  <div class="icon-badge" style="left:494px;top:351px">
    <svg width="32" height="32" viewBox="0 0 32 32" fill="#fff">
      <circle cx="16" cy="16" r="5"/>
      <g stroke="#fff" stroke-width="3" stroke-linecap="round">
        <path d="M16 2v4M16 26v4M2 16h4M26 16h4M6 6l3 3M23 23l3 3M26 6l-3 3M9 23l-3 3"/>
      </g>
    </svg>
  </div>

  <div class="banner">
    <svg width="410" height="68" viewBox="0 0 410 68">
      <polygon points="0,0 410,0 380,34 410,68 0,68 30,34" fill="var(--accent)"/>
    </svg>
    <div class="banner-title">OUR SERVICE</div>
  </div>

  <ul class="features left">
    <li>Automated, Easy</li>
    <li>No clutter or dangling cables on the wall</li>
    <li>4k guarantee</li>
  </ul>
  <div class="divider"></div>
  <ul class="features right">
    <li>Clean, hidden cables. Easy,</li>
    <li>Fully Tested and ready to go</li>
    <li>Just Plug in and way go DIY When you move in to your home</li>
  </ul>

  <div class="product-box"></div>
  <svg class="product-strip" viewBox="0 0 792 128">
    <defs>
      <linearGradient id="panelBlue" x1="0" y1="0" x2="0" y2="1">
        <stop offset="0" stop-color="var(--accent)"/><stop offset="1" stop-color="var(--accent-deep)"/>
      </linearGradient>
    </defs>
    <polygon points="58,0 270,0 240,128 58,128" fill="url(#panelBlue)" role="img" aria-label="Braided HDMI cable with gold connector"/>
    <polygon points="282,0 510,0 486,128 252,128" fill="url(#panelBlue)" role="img" aria-label="Two Brimz HDMI cable plugs"/>
    <polygon points="522,0 738,0 738,128 498,128" fill="url(#panelBlue)" role="img" aria-label="White HDMI wall plate input"/>
  </svg>

  <p class="rooms-title">Product is used in the following rooms:</p>
  <p class="rooms">
    <span class="tick">Home theatre</span> <span class="tick">Dining / living room</span> <span class="tick">Fire place</span> <span class="tick">Alfresco</span><br>
    cabana <span class="tick">Pool house</span> <span class="tick">Office</span>
  </p>

  <p class="tagline"><span class="quote-mark">&ldquo;</span> Choosing the right HDMI Cable to<br>prewire hasn't been easier <span class="quote-mark">&rdquo;</span></p>
</main>
</body>
</html>
```